New south Australia high-end red wine label & logo design

Marvick Estate exports premium south Australian wine to oversea market. We are looking for a professional graphic designer to design a full set of wine label and logo for our new red wine, the label & logo should look 'high-end' & Luxury and attractive. Black & gold color is preferred. I have attached example images to demonstrate the feel that we are looking for. These are just a possible starting point. The expectation is that the label would be professional/polished. I am open to any and all designs that would alter my perception of what will be best!

Target customer -

we need the label to be print-ready.

There will be 3 parts to this design.

Top Cover design with gold text wrapped, the front label and the back label

-Brand name Marvik Estate
-text wine of Australia
-text Cabernet
-Year 2015
-text Sourced from premium Australian wine growing region Merrigal valley

Look and Feel:
• Elegant
• Serious
• Modern/Traditional
• Professional
• Gender Neutral
• Upmarket

--------------Back Label text---------------
Rich and opulent with intense fruit aromas of black berry, liquorice and cassis with hints of dark chocolate and pungent spices. Sumptuous and textured palate with beautifully detailed ripe black fruits flowing seamlessly across the palate. French oak provides a complex harmony and finish of great length, balance and purity.

Produced by Rolk Haven Group International Pty Ltd
27 Fellmore Road,Quandip, South Australia, 5172
14.5 ALC/VOL
Wine of Australia
Approx 8.3 Standard Drinks
Contains Sulphites
750 ML
Please leave the space for Bar Code

Requirements
Must have
• wine name, wine logo, wine type etc (should include all 'must-have the required fields wine lable)
Nice to have
• Desginer's own idea
Should not have
• should not be too playful

```html
<!DOCTYPE html>
<html lang="en">
<head>
<meta charset="utf-8">
<title>Marvik Estate – Cabernet 2015 Labels</title>
<link href="https://fonts.googleapis.com/css2?family=Cinzel:wght@400;700&family=EB+Garamond:wght@400&family=Pinyon+Script&family=Oswald:wght@300;400&display=swap" rel="stylesheet">
<style>
  :root {
    --page: #ffffff;
    --label-black: #1b1b1b;
    --gold: #c9a96a;
    --gold-light: #e2c98f;
    --gold-dim: #a88d58;
  }
  * { box-sizing: border-box; margin: 0; padding: 0; }
  html, body { width: 1200px; height: 1200px; overflow: hidden; background: var(--page); }
  .canvas { position: relative; width: 1200px; height: 1200px; }

  .label {
    position: absolute;
    top: 194px;
    width: 480px;
    height: 812px;
    background: var(--label-black);
    color: var(--gold);
  }
  .label--front { left: 80px; }
  .label--back { left: 640px; }

  .label__frame {
    position: absolute;
    inset: 18px;
    border: 3px solid var(--gold);
  }
  .label__frame::after {
    content: "";
    position: absolute;
    inset: 5px;
    border: 1px solid var(--gold);
  }

  .block { position: absolute; left: 0; right: 0; text-align: center; }

  .brand {
    font-family: "Cinzel", serif;
    font-weight: 700;
    color: var(--gold-light);
    letter-spacing: -1px;
    line-height: 1;
  }
  .region {
    font-family: "Cinzel", serif;
    font-weight: 400;
    font-size: 14px;
    letter-spacing: 3px;
    color: var(--gold-dim);
  }
  .script {
    font-family: "Pinyon Script", cursive;
    color: var(--gold-light);
    line-height: 1;
  }
  .rule {
    position: absolute;
    height: 1px;
    background: var(--gold-dim);
  }

  /* Front label */
  .mark { top: 100px; display: flex; flex-direction: column; align-items: center; gap: 10px; }
  .mark__circle { width: 72px; height: 72px; border: 2px solid var(--gold); border-radius: 50%; }
  .mark__name { font-family: "Cinzel", serif; font-weight: 400; font-size: 18px; letter-spacing: 2px; color: var(--gold); }
  .origin { top: 262px; font-family: "Cinzel", serif; font-size: 15px; letter-spacing: 1px; color: var(--gold); }
  .label--front .brand { top: 385px; font-size: 54px; }
  .label--front .region { top: 470px; }
  .vintage-front { top: 520px; font-size: 36px; }
  .label--front .rule--left { top: 542px; left: 60px; width: 110px; }
  .label--front .rule--right { top: 542px; right: 60px; width: 110px; }
  .varietal-front { top: 568px; font-size: 46px; }
  .sourced {
    top: 680px;
    font-family: "Cinzel", serif;
    font-size: 17px;
    line-height: 36px;
    color: var(--gold);
  }

  /* Back label */
  .label--back .brand { top: 75px; font-size: 52px; }
  .label--back .region { top: 152px; }
  .varietal-back { top: 200px; font-size: 34px; }
  .label--back .rule--full { top: 252px; left: 120px; width: 240px; }
  .tasting {
    top: 282px;
    left: 52px;
    right: 52px;
    font-family: "EB Garamond", serif;
    font-size: 14.5px;
    line-height: 22px;
    color: var(--gold);
  }
  .tasting p + p { margin-top: 12px; }

  .barcode-space {
    position: absolute;
    top: 624px;
    left: 52px;
    width: 140px;
    height: 118px;
    border: 1px solid var(--gold);
    display: flex;
    align-items: center;
    justify-content: center;
    font-family: "Oswald", sans-serif;
    font-weight: 300;
    font-size: 18px;
    color: var(--gold);
  }

  .details {
    position: absolute;
    top: 620px;
    right: 96px;
    width: 180px;
    text-align: right;
    font-family: "Oswald", sans-serif;
    color: var(--gold);
  }
  .details__abv { font-weight: 300; font-size: 24px; line-height: 1.2; }
  .details__note { font-weight: 300; font-size: 13px; color: var(--gold-dim); margin-top: 2px; }
  .details__volume { font-family: "EB Garamond", serif; font-size: 24px; margin-top: 20px; }

  .drinks { position: absolute; top: 620px; right: 36px; width: 48px; height: 126px; }
  .drinks__caption {
    position: absolute;
    left: 0;
    bottom: 0;
    transform-origin: left bottom;
    transform: rotate(-90deg) translate(0, 14px);
    white-space: nowrap;
    font-family: "Oswald", sans-serif;
    font-weight: 400;
    font-size: 11px;
    color: var(--gold);
  }
  .drinks__icon { position: absolute; right: 0; top: 0; }
</style>
</head>
<body>
<main class="canvas">

  <section class="label label--front" aria-label="Front label">
    <div class="label__frame"></div>
    <div class="block mark">
      <span class="mark__circle"></span>
      <span class="mark__name">Marvik Estate</span>
    </div>
    <p class="block origin">Wine of Australia</p>
    <h1 class="block brand">Marvik Estate</h1>
    <p class="block region">Merrigal Valley</p>
    <span class="rule rule--left"></span>
    <p class="block script vintage-front">2015</p>
    <span class="rule rule--right"></span>
    <p class="block script varietal-front">Cabernet</p>
    <p class="block sourced">Sourced from premium Australian<br>wine growing region Merrigal valley</p>
  </section>

  <section class="label label--back" aria-label="Back label">
    <div class="label__frame"></div>
    <h2 class="block brand">Marvik Estate</h2>
    <p class="block region">Merrigal Valley</p>
    <p class="block script varietal-back">Cabernet 2015</p>
    <span class="rule rule--full"></span>
    <div class="block tasting">
      <p>Rich and opulent with intense fruit aromas of black berry, liquorice and cassis with hints of dark chocolate and pungent spices. Sumptuous and textured palate with beautifully detailed ripe black fruits flowing seamlessly across the palate.</p>
      <p>French oak provides a complex harmony and finish of great length, balance and purity.</p>
      <p>Produced by Rolk Haven Group International Pty Ltd, 27 Fellmore Road, Quandip, South Australia, 5172. Wine of Australia.</p>
    </div>
    <div class="barcode-space">bar code</div>
    <div class="details">
      <p class="details__abv">14.5% Alc/Vol</p>
      <p class="details__note">Contains Sulphites</p>
      <p class="details__volume">750 ML</p>
    </div>
    <div class="drinks">
      <span class="drinks__caption">Approx Standard Drinks</span>
      <svg class="drinks__icon" width="26" height="120" viewBox="0 0 26 120" aria-label="Approx 8.3 standard drinks">
        <path d="M2 2 H24 V30 Q24 50 13 52 Q2 50 2 30 Z" fill="none" stroke="#c9a96a" stroke-width="2"/>
        <line x1="13" y1="52" x2="13" y2="112" stroke="#c9a96a" stroke-width="2"/>
        <line x1="3" y1="113" x2="23" y2="113" stroke="#c9a96a" stroke-width="3"/>
        <text x="13" y="28" text-anchor="middle" font-family="Oswald, sans-serif" font-size="12" fill="#c9a96a">8.3</text>
      </svg>
    </div>
  </section>

</main>
</body>
</html>
```